Sleek Design For Personal Brand Wordpress Website !!

*WORDPRESS WEBSITE*

Need a sleek and easy to navigate Wordpress website.

It will act as the hub for my personal brand.

Which means it will showcase all my social media outlets, host my most recent content like vidstream videos and podcasts...

It will also be the go to place to find all my digital products and services that I offer.

i want it to be super sleek and simple but also give a personal touch of my who I really am. You can get a good idea of who I am my checking out my Picturely (@karim.delouve)

Use these websites for ideas: www.brodyvance.example and www.nolanfitzbergen.example

Target Market(s)

Young Entrepreneurs

Industry/Entity Type

Education

Logo Text

Karim Delouve

Number of Pages Required

4 page

Font styles to use
Sans Serif

Colors
ffffff
0392cd
ec1f27

Requirements
Must have
• Social Media buttons on the home page...
• Video (also a slider) right at the top of the home page...
• Email Optin...
• Multiple pages...

```html
<!DOCTYPE html>
<html lang="en">
<head>
<meta charset="utf-8">
<title>Karim Delouve — Personal Brand</title>
<link rel="stylesheet" href="https://fonts.googleapis.com/css2?family=Oswald:wght@400;500&family=Open+Sans:wght@400;600&display=swap">
<style>
:root{
  --blue:#0392cd;
  --red:#ec1f27;
  --white:#ffffff;
  --ink:#3a3a3a;
  --muted:#7a7a7a;
  --line:#e3e3e3;
  --dark:#1b1b1b;
  --darker:#0e0e0e;
}
*{box-sizing:border-box;margin:0;padding:0}
html,body{width:1200px;height:2469px;overflow:hidden;background:var(--white)}
body{font-family:"Open Sans",Arial,sans-serif;color:var(--ink);position:relative}

/* header */
.site-header{height:44px;position:relative}
.brand{position:absolute;left:249px;top:6px;font-family:"Oswald",sans-serif;font-weight:500;font-size:19px;color:var(--blue);letter-spacing:.5px;line-height:1}
.brand-dot{display:inline-block;width:10px;height:10px;background:var(--red);margin-right:6px;vertical-align:1px}
.header-social{position:absolute;right:250px;top:2px;display:flex;gap:8px}
.header-social span{width:14px;height:14px;border-radius:50%;background:var(--blue)}
.main-nav{position:absolute;right:250px;top:26px;display:flex;gap:9px;font-family:"Oswald",sans-serif;font-size:10px;color:#555}
.main-nav a{color:inherit;text-decoration:none}
.main-nav a.active{color:var(--red);border-bottom:2px solid var(--red);padding-bottom:1px}

/* hero */
.hero{height:372px;position:relative;background:linear-gradient(90deg,#c9c2b8 0%,#8c7a6b 22%,#3d3530 45%,#5a5f66 70%,#c8ccd0 100%)}
.hero-copy{position:absolute;left:650px;top:118px;width:300px;text-align:right;color:var(--white);font-family:"Oswald",sans-serif}
.hero-kicker{font-size:14px}
.hero-title{font-size:19px;font-weight:500;margin-top:6px;letter-spacing:.3px}
.hero-video{position:absolute;left:657px;top:178px;width:293px;height:145px;border:2px solid var(--red);background:linear-gradient(135deg,#3a2a2a,#7d1c1c 55%,#2b2b2b)}

.play{position:absolute;left:50%;top:50%;transform:translate(-50%,-50%)}

/* features */
.feature{position:absolute;width:701px;left:249px}
.feature-text{position:absolute;top:0;width:348px}
.feature h2{font-family:"Oswald",sans-serif;font-weight:500;font-size:16px;line-height:22px;color:#4a4a4a}
.feature p{font-size:10px;line-height:16px;color:var(--muted);margin-top:10px}
.btn{display:inline-block;background:var(--red);color:var(--white);font-family:"Oswald",sans-serif;font-size:11px;text-decoration:none;text-align:center;border-radius:2px}
.feature .btn{position:absolute;width:100px;height:26px;line-height:26px}
.media{position:absolute;background:linear-gradient(135deg,#5a1a1a,#b02a2a 50%,#2b1d1d)}

/* subscribe */
.subscribe{position:absolute;left:0;top:862px;width:1200px;height:70px;background:linear-gradient(100deg,#bfe6f7 0%,#1aa6de 25%,#0b8fd0 50%,#2bb0e6 75%,#bfe6f7 100%);display:flex;align-items:center;justify-content:center;gap:12px}
.subscribe-label{font-family:"Oswald",sans-serif;font-size:16px;color:var(--white);margin-right:2px}
.subscribe-input{width:201px;height:26px;background:var(--white);border:1px solid #ddd;font-size:9px;color:#aaa;padding:0 7px;line-height:26px}
.subscribe .btn{width:100px;height:26px;line-height:26px}

/* section titles */
.section-title{position:absolute;left:0;width:1200px;text-align:center;font-family:"Oswald",sans-serif;font-weight:400;font-size:16px;color:#555}
.section-title::after{content:"";display:block;width:38px;height:2px;background:var(--blue);margin:6px auto 0}

/* podcast grid */
.podcast-grid{position:absolute;left:249px;top:1002px;width:701px;display:grid;grid-template-columns:repeat(3,228px);column-gap:9px;row-gap:16px}
.episode{height:216px;border:1px solid var(--line);background:var(--white)}
.episode-date{height:20px;font-size:8px;color:#888;padding:4px 9px}
.episode-thumb{height:150px;position:relative}
.episode-title{font-family:"Oswald",sans-serif;font-weight:400;font-size:14px;line-height:16px;color:var(--blue);padding:4px 6px}

/* stay in touch */
.touch{position:absolute;left:0;top:1712px;width:1200px;height:173px;background:radial-gradient(circle at 0% 50%,#e3e6fb 0,#f7f8fc 25%,#fff 45%),#fff}
.touch-icons{position:absolute;left:301px;top:80px;display:flex;gap:24px}
.touch-icons span{width:54px;height:54px;border:1.5px solid var(--blue);border-radius:6px;display:flex;align-items:center;justify-content:center;background:var(--white)}
.touch-icons span::before{content:"";width:12px;height:12px;border-radius:50%;background:var(--blue)}
.touch-icons span.is-active{background:var(--red);border-color:var(--red)}
.touch-icons span.is-active::before{background:var(--white)}

/* social panels */
.panels{position:absolute;left:258px;top:1960px;display:flex;gap:13px}
.panel{width:219px;height:270px;border:1px solid var(--line);padding:8px 10px}
.panel h3{font-family:"Oswald",sans-serif;font-weight:400;font-size:14px;color:var(--blue);text-align:center}
.panel-body{margin-top:10px;height:220px}
.photo-grid{background:linear-gradient(135deg,#d9c8bc,#8a6d5e 40%,#c4b3a6 70%,#5e4a40)}
.feed{border:1px solid #eee;padding:10px}
.feed-line{height:7px;background:#e6e6e6;margin-bottom:10px;border-radius:2px}
.feed-line.short{width:55%}
.feed-line.accent{background:#cfe8f4;width:40%}
.video-feed{background:linear-gradient(180deg,#3b3b3b 0,#6b5b4f 30%,#f1f1f1 30%,#f1f1f1 62%,#2d2d2d 62%)}

/* footer */
.site-footer{position:absolute;left:0;top:2267px;width:1200px;height:173px;background:linear-gradient(135deg,#222,#141414 50%,#202020)}
.footer-col{position:absolute;top:24px}
.footer-col h4{font-family:"Open Sans",sans-serif;font-weight:600;font-size:12px;color:var(--white);margin-bottom:6px}
.footer-col a{display:block;font-size:9.5px;line-height:21px;color:#d6d6d6;text-decoration:none}
.footer-bar{position:absolute;left:0;top:2440px;width:1200px;height:29px;background:var(--darker);font-size:8.5px;color:#ddd}
.footer-bar .copy{position:absolute;left:249px;top:9px}
.footer-bar nav{position:absolute;right:250px;top:9px;display:flex;gap:8px}
.footer-bar nav a{color:#ddd;text-decoration:none}
</style>
</head>
<body>

<header class="site-header">
  <div class="brand"><span class="brand-dot"></span>KARIM DELOUVE</div>
  <div class="header-social" aria-label="Social links"><span></span><span></span><span></span></div>
  <nav class="main-nav">
    <a class="active" href="#">HOME</a><a href="#">ABOUT ME</a><a href="#">BOOKS</a><a href="#">SERVICES</a><a href="#">PODCAST</a><a href="#">BLOG</a><a href="#">EVENTS</a><a href="#">CONTACT ME</a>
  </nav>
</header>

<section class="hero" role="img" aria-label="Man with glasses working at a computer in a dim office">
  <div class="hero-copy">
    <div class="hero-kicker">Learn How To Create An Online Business From Scratch!</div>
    <div class="hero-title">HOW I MAKE MONEY ONLINE</div>
  </div>
  <div class="hero-video" role="img" aria-label="Video still of a speaker on a conference stage">
    <svg class="play" width="40" height="40" viewBox="0 0 40 40"><circle cx="20" cy="20" r="18" fill="none" stroke="#fff" stroke-opacity=".6" stroke-width="2"/><path d="M16 12l12 8-12 8z" fill="#fff" fill-opacity=".6"/></svg>
  </div>
</section>

<article class="feature" style="top:453px;height:171px">
  <div class="feature-text" style="left:0">
    <h2>Penatibus et magnis dis parturient montes, nascetur ridiculus mus</h2>
    <p>Lorem ipsum dolor sit amet, consectetur adipiscing elit. Nulla ut odio quis dui pellentesque convallis quis vitae justo. Orci varius natoque penatibus et magnis dis parturient montes, nascetur ridiculus mus. Vivamus fringilla condimentum sodales. Duis mattis quis lorem vitae placerat. Maecenas ac nibh neque.</p>
  </div>
  <a class="btn" href="#" style="left:0;top:146px">Read More</a>
  <div class="media" style="left:386px;top:0;width:315px;height:171px" role="img" aria-label="Speaker on a red-curtained stage before an audience">
    <svg class="play" width="38" height="28" viewBox="0 0 38 28"><rect width="38" height="28" rx="7" fill="var(--red)"/><path d="M15 8l10 6-10 6z" fill="#fff"/></svg>
  </div>
</article>

<article class="feature" style="top:660px;height:171px">
  <div class="media" style="left:0;top:0;width:316px;height:171px;background:linear-gradient(135deg,#6f8aa3,#2e3d4d 45%,#1b1b1b 70%,#b9b9b9)" role="img" aria-label="Person with headphones at a keyboard beside a podcast phone">
    <svg class="play" width="38" height="28" viewBox="0 0 38 28"><rect width="38" height="28" rx="7" fill="var(--red)"/><path d="M15 8l10 6-10 6z" fill="#fff"/></svg>
  </div>
  <div class="feature-text" style="left:353px">
    <h2>Penatibus et magnis dis parturient montes, nascetur ridiculus mus</h2>
    <p>Lorem ipsum dolor sit amet, consectetur adipiscing elit. Nulla ut odio quis dui pellentesque convallis quis vitae justo. Orci varius natoque penatibus et magnis dis parturient montes, nascetur ridiculus mus. Vivamus fringilla condimentum sodales. Duis mattis quis lorem vitae placerat. Maecenas ac nibh neque.</p>
  </div>
  <a class="btn" href="#" style="left:353px;top:146px">Read More</a>
</article>

<section class="subscribe">
  <span class="subscribe-label">Subscribe to Get Emial Updates!</span>
  <span class="subscribe-input">Enter Email</span>
  <a class="btn" href="#">Subscribe</a>
</section>

<h2 class="section-title" style="top:958px">Podcast</h2>

<section class="podcast-grid">
  <article class="episode"><div class="episode-date">December 22, 2017</div><div class="episode-thumb" role="img" aria-label="Man beneath chalk-drawn social icons" style="background:linear-gradient(135deg,#555,#8a8a8a 50%,#3e3e3e)"></div><h3 class="episode-title">Duis sed magna gravida, luctus arcu at, viverra lacus.</h3></article>
  <article class="episode"><div class="episode-date">December 24, 2017</div><div class="episode-thumb" role="img" aria-label="Colourful app keys close-up" style="background:linear-gradient(135deg,#c9d6e0,#e8e8e8 45%,#d8585c 70%,#5b8fc7)"></div><h3 class="episode-title">Duis sed magna gravida, luctus arcu at, viverra lacus.</h3></article>
  <article class="episode"><div class="episode-date">December 26, 2017</div><div class="episode-thumb" role="img" aria-label="Hand holding a podcast card over a keyboard" style="background:linear-gradient(135deg,#2b2b2b,#18b7c9 45%,#0e8f9f 70%,#2b2b2b)"></div><h3 class="episode-title">Duis sed magna gravida, luctus arcu at, viverra lacus.</h3></article>
  <article class="episode"><div class="episode-date">December 5, 2017</div><div class="episode-thumb" role="img" aria-label="Laptop and headphones on a desk" style="background:linear-gradient(135deg,#cfcfcf,#6d6d6d 45%,#2f2f2f)"></div><h3 class="episode-title">Duis sed magna gravida, luctus arcu at, viverra lacus.</h3></article>
  <article class="episode"><div class="episode-date">December 5, 2017</div><div class="episode-thumb" role="img" aria-label="Collage of printed social network labels" style="background:linear-gradient(135deg,#e25b5b,#f2efe9 40%,#4aa8e0 70%,#f0c45a)"></div><h3 class="episode-title">Duis sed magna gravida, luctus arcu at, viverra lacus.</h3></article>
  <article class="episode"><div class="episode-date">December 5, 2017</div><div class="episode-thumb" role="img" aria-label="Person in red holding white earphones" style="background:linear-gradient(135deg,#8f1d1d,#d2302e 50%,#6a4a34)"></div><h3 class="episode-title">Duis sed magna gravida, luctus arcu at, viverra lacus.</h3></article>
  <article class="episode"><div class="episode-date">December 5, 2017</div><div class="episode-thumb" role="img" aria-label="Hand holding a phone showing a podcast app" style="background:linear-gradient(135deg,#3a3a3a,#e58a7a 45%,#f2b6a8 65%,#4a4a4a)"></div><h3 class="episode-title">Duis sed magna gravida, luctus arcu at, viverra lacus.</h3></article>
  <article class="episode"><div class="episode-date">December 5, 2017</div><div class="episode-thumb" role="img" aria-label="Two hosts recording at a microphone" style="background:linear-gradient(135deg,#1f3f66,#a88a70 45%,#2b2b2b)"></div><h3 class="episode-title">Duis sed magna gravida, luctus arcu at, viverra lacus.</h3></article>
  <article class="episode"><div class="episode-date">December 5, 2017</div><div class="episode-thumb" role="img" aria-label="Headphones, notebook and red coffee cup on a wooden table" style="background:linear-gradient(135deg,#b77a5a,#d39a78 45%,#c0392b 75%,#a86a4a)"></div><h3 class="episode-title">Duis sed magna gravida, luctus arcu at, viverra lacus.</h3></article>
</section>

<section class="touch">
  <h2 class="section-title" style="top:28px">Stay In Touch With Me.</h2>
  <div class="touch-icons" aria-label="Social network buttons">
    <span></span><span></span><span></span><span class="is-active"></span><span></span><span></span><span></span><span></span>
  </div>
</section>

<h2 class="section-title" style="top:1908px">Social Media</h2>

<section class="panels">
  <div class="panel">
    <h3>Picturely Photos</h3>
    <div class="panel-body photo-grid" role="img" aria-label="Grid of recent Picturely photos"></div>
  </div>
  <div class="panel">
    <h3>Recent Chirps</h3>
    <div class="panel-body feed">
      <div class="feed-line accent"></div>
      <div class="feed-line"></div>
      <div class="feed-line short"></div>
      <div class="feed-line"></div>
      <div class="feed-line short"></div>
      <div class="feed-line accent"></div>
      <div class="feed-line"></div>
      <div class="feed-line"></div>
      <div class="feed-line short"></div>
    </div>
  </div>
  <div class="panel">
    <h3>Friendhub Posts</h3>
    <div class="panel-body video-feed" role="img" aria-label="Friendhub page feed with video posts"></div>
  </div>
</section>

<footer class="site-footer">
  <div class="footer-col" style="left:249px"><h4>News &amp; Media</h4><a href="#">Latest Stories</a><a href="#">Press Releases</a><a href="#">Media Inquiries</a><a href="#">Media Partners</a><a href="#">The News</a></div>
  <div class="footer-col" style="left:435px"><h4>Support</h4><a href="#">Latest Stories</a><a href="#">Press Releases</a><a href="#">Media Inquiries</a><a href="#">Media Partners</a><a href="#">The News</a></div>
  <div class="footer-col" style="left:609px"><h4>Event</h4><a href="#">Latest Stories</a><a href="#">Press Releases</a><a href="#">Media Inquiries</a><a href="#">Media Partners</a><a href="#">The News</a></div>
  <div class="footer-col" style="left:765px"><h4>News &amp; Media</h4><a href="#">Submit Your Story</a><a href="#">Member Updates Archive</a><a href="#">Contact</a><a href="#">Login</a></div>
</footer>
<div class="footer-bar">
  <span class="copy">© 2017 . All Rights Reserved.</span>
  <nav><a href="#">HOME</a><a href="#">ABOUT ME</a><a href="#">BOOKS</a><a href="#">SERVICES</a><a href="#">PODCAST</a><a href="#">BLOG</a><a href="#">EVENTS</a><a href="#">CONTACT ME</a></nav>
</div>

</body>
</html>
```